Label for new gin: Kliff7 - Distilled Gin

Artistic label with local elements for new gin brand.
Dunes, lighthouses, sea, seagulls, ships.
Fresh lemon gin with fine juniper notes. Manufactured directly on the Baltic Sea in Klipphafen. Should be scalable. 4x6inch or larger.
Motifs put together artistically. Photos of the place in the attachment. The name of the gin comes from the beach entrance 3 (hence dune 3). A dune stalk (blue oat) is in the bottle. Bottle will be a clear glass apothecary bottle 500ml.
Updates

Niedrige Design-Qualität

Target Market(s)

spirits

Industry/Entity Type

Getränke

Font styles to use
Decorative
Script

Colors

Designer to choose colors to be used in the design.

Requirements
Must have
• Sketch, Handdrawn Style /// 500ml, 41% vol Alc "Made by QMTO GmbH Farnstieg 22a Hallentin" "Bottled in Klipphafen" "Kliff7" "Distilled Gin" "Inspired by the sea"

```html
<!DOCTYPE html>
<html lang="de">
<head>
<meta charset="utf-8">
<title>Kliff7 Distilled Gin – Label Variants</title>
<link rel="stylesheet" href="https://fonts.googleapis.com/css2?family=IM+Fell+English+SC&family=Rye&family=Kaushan+Script&family=Cinzel:wght@700&family=Stardos+Stencil:wght@700&family=Lobster&family=Oswald:wght@500&display=swap">
<style>
  :root {
    --page: #ffffff;
    --sky: #eef1f3;
    --art-light: #f2f3f4;
    --art-mid: #e3e4e5;
    --art-deep: #d2d3d4;
    --ink: #333333;
    --ink-soft: #555555;
    --gold: #a8922f;
    --band-outer: #3a3a3a;
    --band-inner: #474747;
    --band-text: #f4f4f4;
  }
  * { margin: 0; padding: 0; box-sizing: border-box; }
  html, body { width: 1200px; height: 802px; overflow: hidden; background: var(--page); }
  .canvas { position: relative; width: 1200px; height: 802px; }

  .label {
    position: absolute; top: 38px; width: 543px; height: 742px;
    overflow: hidden; text-align: center; color: var(--ink);
  }
  .label--dunes { left: 40px; }
  .label--harbour { left: 617px; }

  .label__art { position: absolute; left: 0; top: 0; width: 543px; height: 650px; }
  .label--dunes .label__art {
    background: linear-gradient(180deg, var(--sky) 0 125px, var(--art-light) 125px, var(--art-light) 250px, var(--art-mid) 420px, var(--art-light) 520px, var(--art-deep) 650px);
  }
  .label--harbour .label__art {
    background:
      linear-gradient(90deg, transparent 0 68%, rgba(210,212,214,.45) 80%, rgba(200,202,204,.5) 100%),
      linear-gradient(180deg, var(--sky) 0 118px, var(--art-light) 118px, var(--art-light) 420px, var(--art-mid) 470px, var(--art-light) 560px, var(--art-mid) 650px);
  }

  .label__kicker {
    position: absolute; left: 0; right: 0; top: 70px;
    font-family: "IM Fell English SC", serif; font-size: 29px; line-height: 30px;
    letter-spacing: 1.5px; color: var(--gold);
  }
  .label__brand {
    position: absolute; left: 0; right: 0; top: 178px;
    font-family: "Rye", serif; font-weight: 400; font-size: 108px; line-height: 130px;
    color: var(--ink); letter-spacing: -2px;
  }
  .label__est, .label__proof {
    position: absolute; top: 352px; width: 90px;
    font-family: "Cinzel", serif; font-weight: 700; line-height: 22px;
  }
  .label__est { left: 43px; font-size: 19px; }
  .label__est span { display: block; font-size: 16px; color: var(--ink-soft); }
  .label__proof { left: 404px; font-size: 23px; }
  .label__proof span { display: block; font-family: "IM Fell English SC", serif; font-size: 16px; color: var(--ink-soft); }
  .label__type {
    position: absolute; left: 120px; width: 310px; top: 336px;
    font-family: "Kaushan Script", cursive; font-size: 52px; line-height: 64px; color: #3a3a3a;
    white-space: nowrap;
  }
  .label__origin {
    position: absolute; left: 0; right: 0; top: 480px;
    font-family: "Stardos Stencil", serif; font-weight: 700; font-size: 32px; line-height: 38px;
    letter-spacing: 1px; color: var(--ink);
  }
  .label__tagline {
    position: absolute; left: 0; right: 0; top: 557px;
    font-family: "Lobster", cursive; font-size: 25px; line-height: 30px; color: var(--gold);
  }

  .label__band { position: absolute; left: 0; top: 639px; width: 543px; height: 103px; }
  .band__facts, .band__maker {
    position: absolute; font-family: "Oswald", sans-serif; font-weight: 500; color: var(--band-text);
    text-transform: uppercase; white-space: nowrap;
  }
  .band__facts { left: 40px; width: 120px; top: 662px; font-size: 20px; line-height: 27px; }
  .band__maker { left: 358px; width: 175px; top: 657px; font-size: 14.5px; line-height: 20px; }
</style>
</head>
<body>
<main class="canvas">

  <section class="label label--dunes">
    <div class="label__art" role="img" aria-label="Pencil sketch of Baltic sand dunes in soft grey tones"></div>
    <p class="label__kicker">SMALL BATCH<br>CRAFTED</p>
    <h1 class="label__brand">KLIFF7</h1>
    <p class="label__est">EST<span>2021</span></p>
    <p class="label__type">Distilled Gin</p>
    <p class="label__proof">80<span>PROOF</span></p>
    <p class="label__origin">BOTTLED IN<br>KLIPPHAFEN</p>
    <p class="label__tagline">Inspired By The Sea</p>
    <svg class="label__band" viewBox="0 0 543 103" aria-hidden="true">
      <defs>
        <pattern id="zig-top-a" width="8" height="8" patternUnits="userSpaceOnUse">
          <polygon points="0,8 4,0 8,8" fill="#3a3a3a"/>
        </pattern>
        <pattern id="zig-bottom-a" width="8" height="8" patternUnits="userSpaceOnUse">
          <polygon points="0,0 4,8 8,0" fill="#3a3a3a"/>
        </pattern>
      </defs>
      <rect x="0" y="0" width="543" height="8" fill="url(#zig-top-a)"/>
      <rect x="0" y="8" width="543" height="87" fill="#3a3a3a"/>
      <rect x="0" y="14" width="543" height="70" fill="#474747"/>
      <rect x="0" y="95" width="543" height="8" fill="url(#zig-bottom-a)"/>
      <circle cx="212" cy="50" r="5.6" fill="#f4f4f4"/>
      <circle cx="239" cy="50" r="8.4" fill="#f4f4f4"/>
      <circle cx="271" cy="50" r="11" fill="#f4f4f4"/>
      <circle cx="304" cy="50" r="8.4" fill="#f4f4f4"/>
      <circle cx="331" cy="50" r="5.6" fill="#f4f4f4"/>
    </svg>
    <p class="band__facts">500ML<br>41% VOL/ALC</p>
    <p class="band__maker">MADE BY<br>QMTO GMBH FARNSTIEG<br>22A HALLENTIN</p>
  </section>

  <section class="label label--harbour">
    <div class="label__art" role="img" aria-label="Pencil sketch of a harbour with lighthouse, sailboat, ship and breakwater stones"></div>
    <p class="label__kicker">SMALL BATCH<br>CRAFTED</p>
    <h2 class="label__brand">KLIFF7</h2>
    <p class="label__est">EST<span>2021</span></p>
    <p class="label__type">Distilled Gin</p>
    <p class="label__proof">80<span>PROOF</span></p>
    <p class="label__origin">BOTTLED IN<br>KLIPPHAFEN</p>
    <p class="label__tagline">Inspired By The Sea</p>
    <svg class="label__band" viewBox="0 0 543 103" aria-hidden="true">
      <defs>
        <pattern id="zig-top-b" width="8" height="8" patternUnits="userSpaceOnUse">
          <polygon points="0,8 4,0 8,8" fill="#3a3a3a"/>
        </pattern>
        <pattern id="zig-bottom-b" width="8" height="8" patternUnits="userSpaceOnUse">
          <polygon points="0,0 4,8 8,0" fill="#3a3a3a"/>
        </pattern>
      </defs>
      <rect x="0" y="0" width="543" height="8" fill="url(#zig-top-b)"/>
      <rect x="0" y="8" width="543" height="87" fill="#3a3a3a"/>
      <rect x="0" y="14" width="543" height="70" fill="#474747"/>
      <rect x="0" y="95" width="543" height="8" fill="url(#zig-bottom-b)"/>
      <circle cx="212" cy="50" r="5.6" fill="#f4f4f4"/>
      <circle cx="239" cy="50" r="8.4" fill="#f4f4f4"/>
      <circle cx="271" cy="50" r="11" fill="#f4f4f4"/>
      <circle cx="304" cy="50" r="8.4" fill="#f4f4f4"/>
      <circle cx="331" cy="50" r="5.6" fill="#f4f4f4"/>
    </svg>
    <p class="band__facts">500ML<br>41% VOL/ALC</p>
    <p class="band__maker">MADE BY<br>QMTO GMBH FARNSTIEG<br>22A HALLENTIN</p>
  </section>

</main>
</body>
</html>
```